Business card design for Kovantrix

I need a business card based on the logo design produced for Kovantrix. The company is focused on triathlon and endurance sport coaching and the tag line is (per the logo) "Stamina. Discipline. Progression". The design should be sophisticated, appropriate to an affluent and business oriented target market. Colors are optional but the color of the logo probably dictates the color used on the card. I envisage using the red logo, with black print for the wording and contact numbers on a white or cream background, but am open to alternative suggestions. I expect to select something fairly conventional, but would like to see some designs that are less conventional to stretch my thinking on what could be appropriate. I am assuming a single side design is best, but willing to consider double sided as an option.

Target Market(s)

Individual athletes and corporate health and wellness leaders

Industry/Entity Type

Health And Wellness

Contact Information for Business Card

The card should provide the following information:
Logo
My name: Marcus Bellingham
Company website: Kovantrix.com
My email: marcus.bellingham@kovantrix.com
My cell phone number: +1-555-812-6093

Font styles to use
Sans Serif

Colors

Designer to choose colors to be used in the design.

Requirements
Must have
• Space on the card - simple design, not over crowded.
Nice to have
• clean and clear font, nothing garish or mass market like
Should not have
• Do not add pictures

```html
<!DOCTYPE html>
<html lang="en">
<head>
<meta charset="utf-8">
<title>Kovantrix Business Card</title>
<link rel="stylesheet" href="https://fonts.googleapis.com/css2?family=Jost:wght@400;600&display=swap">
<style>
  :root {
    --red: #b5121b;
    --ink: #1a1a1a;
    --card-black: #0b0b0b;
    --card-white: #fbfbfb;
    --ghost: #e6e6e6;
    --stage: #eeeae4;
    --tagline: #f2f2f2;
  }
  * { box-sizing: border-box; margin: 0; padding: 0; }
  html, body {
    width: 1200px; height: 800px; overflow: hidden;
    background: var(--stage);
    font-family: "Jost", sans-serif;
  }
  .canvas { position: relative; width: 1200px; height: 800px; }
  .card {
    position: absolute;
    width: 520px; height: 297px;
    box-shadow: 0 10px 28px rgba(0,0,0,0.18);
  }
  /* front */
  .card--front {
    left: 70px; top: 140px;
    background: var(--card-black);
    display: flex; flex-direction: column; align-items: center; justify-content: center;
  }
  .brand {
    display: flex; align-items: center; gap: 14px;
    color: var(--red); font-weight: 600; font-size: 68px; line-height: 1;
    letter-spacing: -0.5px;
  }
  .brand__dot {
    width: 22px; height: 22px; border-radius: 50%; background: var(--red);
  }
  .tagline {
    margin-top: 10px;
    color: var(--tagline); font-size: 19px; font-weight: 400;
    letter-spacing: 1px; text-transform: uppercase;
  }
  /* back */
  .card--back {
    left: 610px; top: 360px;
    background: var(--card-white);
    padding: 34px 36px;
  }
  .holder {
    font-size: 21px; font-weight: 400; color: var(--ink);
    text-transform: uppercase; letter-spacing: 0.3px;
  }
  .holder__surname { color: var(--red); font-weight: 600; }
  .ghost-mark {
    position: absolute; left: 40px; top: 92px;
    font-size: 86px; font-weight: 600; color: var(--ghost);
    letter-spacing: -1px; line-height: 1;
  }
  .contact {
    position: absolute; right: 44px; bottom: 30px;
    text-align: right; color: var(--ink); font-size: 15.5px; line-height: 1.45;
  }
  .contact__social { display: inline-flex; align-items: center; gap: 6px; }
  .contact__dot { width: 13px; height: 13px; border-radius: 50%; background: var(--red); }
  .contact__sep { margin: 0 8px; }
  .accent-bar {
    position: absolute; right: 0; bottom: 26px;
    width: 16px; height: 50px; background: var(--red);
  }
</style>
</head>
<body>
<main class="canvas">
  <section class="card card--front">
    <div class="brand"><span class="brand__dot"></span>Kovantrix</div>
    <p class="tagline">Stamina. Discipline. Progression</p>
  </section>

  <section class="card card--back">
    <h1 class="holder">Marcus <span class="holder__surname">Bellingham</span></h1>
    <div class="ghost-mark" aria-hidden="true">Kovantrix</div>
    <div class="contact">
      <div class="contact__social"><span class="contact__dot"></span>@kovantrix</div>
      <div>+1-555-812-6093<span class="contact__sep">|</span>Kovantrix.com</div>
      <div>marcus.bellingham@kovantrix.com</div>
    </div>
    <span class="accent-bar"></span>
  </section>
</main>
</body>
</html>
```